Design for schnapps bottle label "Sol Terrado"

Hi! On a small land lot we are producing our own Italian schnapps "Grappa". For the bottles we would like to modernize our current labes that you find below. The two cats looking at each other should remain, but updated and more modern. I am very much looking forward to your suggestions. Best, Joel

Target Market(s)

Schnapps bottle label

Requirements
Must have
• Cats should resemble the cats that are decorating the house entry (see attached), however, should have a more modern appearance.

Text elements should remain: "Grappa", "Sol Terrado", "Legnoso", "[Vintage Year], "Raccolta No", "Vol %"
Should not have
• Current ornament can be used, replaced or deleted (whatever looks best)

```html
<!DOCTYPE html>
<html lang="it">
<head>
<meta charset="utf-8">
<title>Grappa Legnoso 2015 – Sol Terrado</title>
<link rel="stylesheet" href="https://fonts.googleapis.com/css2?family=Josefin+Sans:wght@300;400;600&family=Poiret+One&display=swap">
<style>
  :root {
    --paper: #ffffff;
    --ink: #141414;
    --cat-black: #1e1e1e;
    --cat-red: #7a2226;
    --badge-text: #ffffff;
  }
  html, body {
    margin: 0;
    padding: 0;
    overflow: hidden;
    background: var(--paper);
  }
  .label {
    position: relative;
    width: 858px;
    height: 1200px;
    background: var(--paper);
    color: var(--ink);
    overflow: hidden;
    font-family: "Josefin Sans", sans-serif;
  }
  .label__title {
    position: absolute;
    top: 44px;
    left: 0;
    width: 100%;
    margin: 0;
    text-align: center;
    font-weight: 600;
    font-size: 116px;
    letter-spacing: 10px;
    line-height: 1;
  }
  .label__variety {
    position: absolute;
    top: 186px;
    left: 0;
    width: 100%;
    text-align: center;
    font-family: "Poiret One", sans-serif;
    font-size: 40px;
    font-variant: small-caps;
    letter-spacing: 2px;
    color: var(--ink);
  }
  .label__vintage {
    position: absolute;
    top: 280px;
    left: 50%;
    transform: translateX(-50%);
    display: flex;
    gap: 8px;
  }
  .vintage-digit {
    width: 46px;
    height: 46px;
    border-radius: 50%;
    background: var(--ink);
    color: var(--badge-text);
    display: flex;
    align-items: center;
    justify-content: center;
    font-weight: 600;
    font-size: 30px;
    padding-top: 4px;
    box-sizing: border-box;
  }
  .label__of {
    position: absolute;
    top: 385px;
    left: 0;
    width: 100%;
    text-align: center;
    font-family: "Poiret One", sans-serif;
    font-size: 50px;
    font-variant: small-caps;
  }
  .label__cats {
    position: absolute;
    top: 440px;
    left: 43px;
    width: 772px;
    height: 370px;
  }
  .label__brand {
    position: absolute;
    top: 838px;
    left: 0;
    width: 100%;
    margin: 0;
    text-align: center;
    font-weight: 300;
    font-size: 90px;
    letter-spacing: 2px;
    line-height: 1;
    white-space: nowrap;
  }
  .label__footer {
    position: absolute;
    bottom: 48px;
    left: 52px;
    right: 52px;
    display: flex;
    justify-content: space-between;
    font-family: "Poiret One", sans-serif;
    font-size: 34px;
    letter-spacing: 1px;
  }
</style>
</head>
<body>
  <main class="label">
    <h1 class="label__title">GRAPPA</h1>
    <div class="label__variety">“Legnoso”</div>
    <div class="label__vintage" aria-label="2015">
      <span class="vintage-digit">2</span>
      <span class="vintage-digit">0</span>
      <span class="vintage-digit">1</span>
      <span class="vintage-digit">5</span>
    </div>
    <div class="label__of">Di</div>

    <svg class="label__cats" viewBox="0 0 772 370" role="img" aria-label="Illustration of two arched black cats with red accents facing each other">
      <defs>
        <linearGradient id="catTone" x1="0" y1="0" x2="0" y2="1">
          <stop offset="0" stop-color="var(--cat-black)"/>
          <stop offset="1" stop-color="var(--cat-red)"/>
        </linearGradient>
      </defs>
      <rect class="cat-area cat-area--left" x="0" y="0" width="350" height="370" rx="40" fill="url(#catTone)"/>
      <rect class="cat-area cat-area--right" x="422" y="0" width="350" height="370" rx="40" fill="url(#catTone)"/>
    </svg>

    <h2 class="label__brand">SOL TERRADO</h2>

    <footer class="label__footer">
      <span class="label__batch">Raccolta No.01</span>
      <span class="label__abv">41.0 %Vol.</span>
    </footer>
  </main>
</body>
</html>
```